Property management company looking for modern card design

We at Blue Maple Holdings provides property management services for its residential and commercial properties, with expertise in all categories of multifamily, industrial and office projects throughout California.

We need a business card design that is professional and modern designed business card. In our field, clients get hundreds of business cards, we would like our card to stand out.

Please avoid small print.

Target Market(s)

Professionals and high end clients

Industry/Entity Type

Financial Planning

Contact Information for Business Card

Company Name: Blue Maple Holdings, Name, email, license #, phone number, website bluemapleholdings.example

Font styles to use
Sans Serif

Requirements
Must have
• The card design needs to be adaptable because there is a possibly we will be expanding into different sectors other than real estate. The card design should be focused on financial planning and asset management.
Nice to have
• Modern and simple business card. Eye catching. Non-standard size/shaped cards would be great.
• bluemapleholdings.example
Should not have
• Too many bright color or any pictures or shapes of real estate stuff.

```html
<!DOCTYPE html>
<html lang="en">
<head>
<meta charset="utf-8">
<title>Blue Maple Holdings – Business Card</title>
<link href="https://fonts.googleapis.com/css2?family=Montserrat:wght@400;600;700&display=swap" rel="stylesheet">
<style>
  :root {
    --page-bg: #e4e4e4;
    --card-bg: #cec3ad;
    --brand-red: #cf2230;
    --ink: #2b2623;
    --ink-soft: #4a433d;
    --card-shadow: rgba(0, 0, 0, 0.18);
  }
  * { margin: 0; padding: 0; box-sizing: border-box; }
  html, body {
    width: 1200px;
    height: 1000px;
    overflow: hidden;
    background: var(--page-bg);
    font-family: "Montserrat", sans-serif;
  }
  .sheet {
    position: relative;
    width: 1200px;
    height: 1000px;
  }
  .card {
    position: absolute;
    left: 250px;
    width: 700px;
    height: 400px;
    background: var(--card-bg);
    border-radius: 36px;
    box-shadow: 0 10px 24px var(--card-shadow);
  }
  .card--front { top: 70px; }
  .card--back  { top: 520px; }

  .brand-name {
    color: var(--brand-red);
    font-weight: 700;
    text-transform: uppercase;
    letter-spacing: 0.04em;
    line-height: 1.1;
  }
  .card--front .brand-name {
    position: absolute;
    left: 60px;
    top: 170px;
    font-size: 30px;
    width: 280px;
  }
  .card--back .brand-name {
    position: absolute;
    left: 0;
    right: 0;
    top: 172px;
    text-align: center;
    font-size: 40px;
  }

  .contact-block {
    position: absolute;
    left: 400px;
    top: 120px;
    color: var(--ink);
  }
  .contact-block .person-name {
    font-size: 26px;
    font-weight: 700;
    letter-spacing: 0.03em;
  }
  .contact-block .job-title {
    font-size: 15px;
    font-weight: 400;
    letter-spacing: 0.08em;
    color: var(--ink-soft);
    margin-top: 4px;
  }
  .contact-list {
    list-style: none;
    margin-top: 26px;
  }
  .contact-list li {
    display: flex;
    align-items: center;
    gap: 12px;
    font-size: 15px;
    color: var(--ink-soft);
    margin-bottom: 12px;
  }
  .contact-list svg {
    width: 16px;
    height: 16px;
    flex: none;
    fill: none;
    stroke: var(--ink);
    stroke-width: 2;
  }
</style>
</head>
<body>
<main class="sheet">
  <section class="card card--front">
    <div class="brand-name">Blue Maple Holdings</div>
    <div class="contact-block">
      <div class="person-name">YOUR NAME</div>
      <div class="job-title">JOB TITLE</div>
      <ul class="contact-list">
        <li>
          <svg viewBox="0 0 24 24"><path d="M5 3h4l2 5-3 2a12 12 0 0 0 6 6l2-3 5 2v4a2 2 0 0 1-2 2A17 17 0 0 1 3 5a2 2 0 0 1 2-2z"/></svg>
          555 - 123 - 8976
        </li>
        <li>
          <svg viewBox="0 0 24 24"><rect x="3" y="5" width="18" height="14" rx="1"/><path d="M3 6l9 7 9-7"/></svg>
          alex@bluemapleholdings.example
        </li>
        <li>
          <svg viewBox="0 0 24 24"><path d="M3 11l9-7 9 7"/><path d="M6 10v10h12V10"/></svg>
          www.bluemapleholdings.example
        </li>
      </ul>
    </div>
  </section>

  <section class="card card--back">
    <div class="brand-name">Blue Maple Holdings</div>
  </section>
</main>
</body>
</html>
```